Staffing/Recruitment company

We need to upgrade our website. At the moment we have a template that was built last year and looks not good at all.
We would like to update it with a new design based on what is popular this year. Including some visual effects etc.
This website is to give all information to our potential clients about what we do, clients with worked in the past, how to contact us and about us.
The website consists of 4 pages.
We would like to see a design that uses the color blue.
The current website is https://brightlanestaff.us/
Logo of the company is uploaded

Some designs were not complete...

```html
<!DOCTYPE html>
<html lang="en">
<head>
<meta charset="utf-8">
<title>Brightlane Staffing</title>
<link href="https://fonts.googleapis.com/css2?family=Bebas+Neue&family=Raleway:wght@400;500;600;700;800&family=Lato:wght@400;700&display=swap" rel="stylesheet">
<style>
:root{
  --navy:#0c0f52;
  --orange:#f26128;
  --ink:#1a1a2e;
  --grey-text:#6b6b78;
  --paper:#ffffff;
  --mist:#f0f0f2;
}
*{margin:0;padding:0;box-sizing:border-box}
html,body{width:1200px;height:2700px;overflow:hidden}
body{position:relative;background:var(--paper);font-family:'Lato',sans-serif;color:var(--ink)}
.abs{position:absolute}
a{text-decoration:none;color:inherit}

/* header */
.site-header{position:absolute;left:0;top:0;width:1200px;height:100px;z-index:10}
.brand{display:flex;align-items:center;gap:8px;font-family:'Raleway',sans-serif;font-weight:800;font-size:15px;color:var(--navy);letter-spacing:.2px}
.brand-square{width:36px;height:36px;background:var(--orange)}
.site-header .brand{left:60px;top:31px}
.main-nav{left:445px;top:34px;display:flex;gap:41px;font-family:'Raleway',sans-serif;font-weight:500;font-size:13px;color:var(--navy)}
.main-nav .current{color:var(--orange)}
.header-call{left:982px;top:25px;width:158px;height:45px;background:var(--orange);color:#fff;display:flex;align-items:center;justify-content:center;gap:7px;font-family:'Raleway',sans-serif;font-weight:600;font-size:13px}

/* hero */
.hero{left:0;top:0;width:1200px;height:695px;background:linear-gradient(90deg,#f4f4f5 0%,#e9eaec 30%,#c8c4c2 55%,#8f8580 80%,#6b6462 100%)}
.hero::after{content:"";position:absolute;inset:0;background:linear-gradient(180deg,rgba(255,255,255,.45) 0%,rgba(255,255,255,0) 40%,rgba(170,120,90,.25) 100%)}
.hero-title{left:57px;top:238px;font-family:'Bebas Neue',sans-serif;font-size:101px;line-height:88px;letter-spacing:3px;z-index:2}
.hero-title .line-navy{color:var(--navy);display:block}
.hero-title .line-orange{color:var(--orange);display:block;letter-spacing:7px}
.btn{display:flex;align-items:center;justify-content:center;font-family:'Raleway',sans-serif;font-weight:700;color:#fff;text-transform:uppercase}
.hero-cta{left:60px;top:457px;width:172px;height:45px;background:var(--navy);font-size:14px;z-index:2}

/* contact band */
.contact-band{left:0;top:695px;width:1200px;height:112px;display:flex}
.contact-band .band-call{width:600px;background:var(--navy)}
.contact-band .band-mail{width:600px;background:var(--orange)}
.band-text{top:728px;display:flex;align-items:center;gap:8px;color:#fff;font-family:'Raleway',sans-serif}
.band-text .label{font-weight:400;font-size:26px;letter-spacing:.3px}
.band-text .value{font-weight:700;font-size:29px}
.band-call-text{left:60px}
.band-mail-text{left:653px}
.band-badge{left:564px;top:713px;width:72px;height:72px;border-radius:50%;background:#fff}

/* about */
.about-bg{left:0;top:807px;width:1200px;height:670px}
.about-photo{left:0;top:807px;width:470px;height:600px;background:radial-gradient(ellipse at 55% 45%,#d9d9dc 0%,#ececee 55%,rgba(240,240,242,0) 80%)}
.eyebrow{font-family:'Raleway',sans-serif;font-weight:600;font-size:12px;color:var(--orange);letter-spacing:.3px}
.about-eyebrow{left:645px;top:960px}
.about-title{left:637px;top:980px;font-family:'Raleway',sans-serif;font-weight:800;font-size:38px;color:var(--navy)}
.about-text{left:637px;top:1037px;width:385px;font-size:11.2px;line-height:19.6px;color:var(--grey-text)}
.about-more{left:636px;top:1203px;width:150px;height:42px;background:var(--orange);font-size:15px;font-weight:600}

/* divisions */
.section-title{left:0;width:1200px;text-align:center;font-family:'Raleway',sans-serif;font-weight:800;color:var(--navy)}
.divisions-title{top:1565px;font-size:39px}
.division-card{top:1648px;width:248px;height:249px;background:#fff;box-shadow:0 0 6px rgba(0,0,0,.09);padding:18px 16px}
.division-card h3{font-family:'Raleway',sans-serif;font-weight:700;font-size:17px;color:var(--navy);margin-bottom:10px}
.division-card p{font-size:11px;line-height:19.5px;color:var(--grey-text)}
.division-card .card-link{position:absolute;left:16px;top:205px;font-family:'Raleway',sans-serif;font-weight:600;font-size:11.5px;color:var(--orange)}

/* career */
.career-mark{left:585px;top:2036px;width:30px;height:30px;background:var(--orange)}
.career-title{top:2105px;font-size:33px;color:#0d0d1f;letter-spacing:-.5px}
.career-text{left:280px;top:2165px;width:600px;text-align:center;font-size:11px;line-height:19.6px;color:var(--grey-text)}
.career-cta{left:497px;top:2257px;width:172px;height:45px;background:var(--orange);font-size:15px;font-weight:600}

/* footer */
.footer-shape{left:0;top:2370px}
.footer-badge{left:548px;top:2385px;width:70px;height:70px;border-radius:50%;background:#fff}
.footer-brand{left:60px;top:2508px;color:#fff}
.footer-brand .brand-square{width:36px;height:36px}
.footer-copy{left:61px;top:2565px;width:230px;font-size:11px;line-height:19.5px;color:#fff}
.footer-copy span{color:var(--orange)}
.social{left:60px;top:2622px;display:flex;gap:8px}
.social i{display:block;width:30px;height:30px;border-radius:50%;background:var(--orange)}
.footer-col{top:2496px;color:#fff;font-size:12.5px}
.footer-col h4{font-family:'Raleway',sans-serif;font-weight:700;font-size:13px;margin-bottom:18px;letter-spacing:.2px}
.link-list{list-style:none;line-height:30px}
.contact-list{list-style:none}
.contact-list li{display:flex;gap:14px;margin-bottom:16px;line-height:19px}
.contact-list svg{flex:none;margin-top:3px}
.newsletter-text{line-height:19px;width:250px}
.newsletter-form{margin-top:18px;width:248px;height:46px;border:1px solid #fff;display:flex;background:var(--navy)}
.newsletter-form span{flex:1;padding:14px 9px;font-size:12.5px}
.newsletter-form button{width:45px;border:0;background:var(--orange);display:flex;align-items:center;justify-content:center}
</style>
</head>
<body>

<section class="hero abs" role="img" aria-label="Photo of three colleagues gathered around a laptop in a bright office"></section>

<header class="site-header">
  <a class="brand abs" href="https://brightlanestaff.us/"><span class="brand-square"></span>BRIGHTLANE STAFFING</a>
  <nav class="main-nav abs">
    <a class="current" href="#">Home</a><a href="#">Clients</a><a href="#">About Us</a><a href="#">Contact us</a>
  </nav>
  <a class="header-call abs" href="#">
    <svg width="15" height="15" viewBox="0 0 24 24"><path fill="#fff" d="M6.6 10.8a15.1 15.1 0 0 0 6.6 6.6l2.2-2.2c.3-.3.7-.4 1-.2 1.1.4 2.3.6 3.6.6.6 0 1 .4 1 1V20c0 .6-.4 1-1 1A17 17 0 0 1 3 4c0-.6.4-1 1-1h3.5c.6 0 1 .4 1 1 0 1.3.2 2.5.6 3.6.1.3 0 .7-.2 1z"/></svg>
    123 456 7890
  </a>
</header>

<h1 class="hero-title abs"><span class="line-navy">How soon can</span><span class="line-orange">You start?</span></h1>
<a class="hero-cta btn abs" href="#">Request a call</a>

<section class="contact-band abs"><div class="band-call"></div><div class="band-mail"></div></section>
<div class="band-text band-call-text abs">
  <span class="label">CALL US NOW</span>
  <svg width="36" height="36" viewBox="0 0 24 24" fill="none" stroke="#fff" stroke-width="1.3"><path d="M6.6 10.8a15.1 15.1 0 0 0 6.6 6.6l2.2-2.2c.3-.3.7-.4 1-.2 1.1.4 2.3.6 3.6.6.6 0 1 .4 1 1V20c0 .6-.4 1-1 1A17 17 0 0 1 3 4c0-.6.4-1 1-1h3.5c.6 0 1 .4 1 1 0 1.3.2 2.5.6 3.6.1.3 0 .7-.2 1z"/><text x="11" y="10" font-size="6" fill="#fff" stroke="none" font-family="Raleway,sans-serif" font-weight="700">24</text></svg>
  <span class="value">123 456 7890</span>
</div>
<div class="band-badge abs"></div>
<div class="band-text band-mail-text abs">
  <span class="label">EMAIL</span>
  <svg width="32" height="24" viewBox="0 0 32 24" fill="none" stroke="#fff" stroke-width="1.6"><rect x="1" y="1" width="30" height="22"/><path d="M1 1l15 12L31 1M1 23l11-10M31 23L20 13"/></svg>
  <span class="value">info@brightlanestaff.us</span>
</div>

<svg class="about-bg abs" width="1200" height="670" viewBox="0 0 1200 670"><polygon points="0,0 1200,0 1200,575 600,670 0,575" fill="#f0f0f2"/></svg>
<div class="about-photo abs" role="img" aria-label="Top-down photo of hands typing on a laptop beside coffee, a plant, a pen and a phone"></div>
<p class="eyebrow about-eyebrow abs">BRIGHTLANE STAFFING</p>
<h2 class="about-title abs">ABOUT US</h2>
<p class="about-text abs">Day in and day out for the last years we've been more than just a staffing company. Throughout this time we've built relationships, we've grown together internally and externally, and have created a system that allows us to personally cater to the needs of our clients and candidates. We've been a mentor for some, a team builder for others, but most importantly we've been there. We know there is no substitute for experience, so let us help you navigate through the ever changing web of talent.</p>
<a class="about-more btn abs" href="#">Read more</a>

<h2 class="section-title divisions-title abs">OUR DIVISIONS</h2>
<article class="division-card abs" style="left:60px">
  <h3>Finance</h3>
  <p>With Wall Street's fast-paced dynamic and ever-changing environment, business demands are always transforming for new and the best talent. Our teams can help alleviate your stresses of recruiting the best...</p>
  <a class="card-link" href="#">READ MORE</a>
</article>
<article class="division-card abs" style="left:337px">
  <h3>Information Technology</h3>
  <p>The technology of today is not going to be the technology of tomorrow, and keeping up with the constant innovation and change would be a full time job – a job our team wakes up every morning ready to take on...</p>
  <a class="card-link" href="#">READ MORE</a>
</article>
<article class="division-card abs" style="left:615px">
  <h3>Healthcare</h3>
  <p>Not only do we provide services to the finance and technology world, we also service the healthcare industry with IT professionals as well. We understand the importance of having the right people behind the right projects...</p>
  <a class="card-link" href="#">READ MORE</a>
</article>
<article class="division-card abs" style="left:892px">
  <h3>Government Projects</h3>
  <p>Navigating the rules and regulations of Government integrators isn't always easy. Our government division, BLGov, recognizes the demands and more importantly, recognizes the solutions. Providing resources in information...</p>
  <a class="card-link" href="#">READ MORE</a>
</article>

<div class="career-mark abs"></div>
<h2 class="section-title career-title abs">JOIN OUR CAREER NETWORK</h2>
<p class="career-text abs">Our Career Network will enhance your job search and application process. Whether you choose to apply or just leave your information, we look forward to staying connected with you.</p>
<a class="career-cta btn abs" href="#">Request a call</a>

<footer>
  <svg class="footer-shape abs" width="1200" height="330" viewBox="0 0 1200 330">
    <polygon points="0,111 583,47 583,330 0,330" fill="#0c0f52"/>
    <polygon points="583,47 620,40 1200,117 1200,330 583,330" fill="#0c0f52"/>
    <polygon points="620,26 1200,99 1200,105 620,32" fill="#f26128"/>
    <polygon points="620,34 1200,107 1200,117 620,42" fill="#ffffff"/>
  </svg>
  <div class="footer-badge abs"></div>

  <a class="brand footer-brand abs" href="#"><span class="brand-square"></span>BRIGHTLANE STAFFING</a>
  <p class="footer-copy abs">© <span>BRIGHTLANE STAFFING</span> - 2022. All Rights Reserved.</p>
  <div class="social abs" aria-label="Social links"><i></i><i></i><i></i></div>

  <div class="footer-col abs" style="left:339px">
    <h4>USEFUL LINKS</h4>
    <ul class="link-list"><li>Home</li><li>Clients</li><li>About Us</li><li>Contact Us</li></ul>
  </div>

  <div class="footer-col abs" style="left:616px">
    <h4>CONTACT INFO</h4>
    <ul class="contact-list">
      <li><svg width="14" height="18" viewBox="0 0 14 18"><path fill="#f26128" d="M7 0a7 7 0 0 0-7 7c0 5 7 11 7 11s7-6 7-11a7 7 0 0 0-7-7zm0 9.5A2.5 2.5 0 1 1 7 4.5a2.5 2.5 0 0 1 0 5z"/></svg><span>Lorem ipsum is simply dummy text<br>and printing typesetting.</span></li>
      <li><svg width="15" height="15" viewBox="0 0 24 24"><path fill="#f26128" d="M6.6 10.8a15.1 15.1 0 0 0 6.6 6.6l2.2-2.2c.3-.3.7-.4 1-.2 1.1.4 2.3.6 3.6.6.6 0 1 .4 1 1V20c0 .6-.4 1-1 1A17 17 0 0 1 3 4c0-.6.4-1 1-1h3.5c.6 0 1 .4 1 1 0 1.3.2 2.5.6 3.6.1.3 0 .7-.2 1z"/></svg><span>123 456 7890</span></li>
      <li><svg width="15" height="12" viewBox="0 0 15 12"><path fill="#f26128" d="M0 0h15v2L7.5 7 0 2zM0 4l7.5 5L15 4v8H0z"/></svg><span>Info@brightlanestaff.us</span></li>
    </ul>
  </div>

  <div class="footer-col abs" style="left:894px">
    <h4>NEWSLETTER</h4>
    <p class="newsletter-text">Subscribe to stya with us and update our recruit, updates etc...</p>
    <div class="newsletter-form">
      <span>Enter email here...</span>
      <button type="button" aria-label="Subscribe"><svg width="18" height="18" viewBox="0 0 24 24"><path fill="#fff" d="M2 11 22 2l-9 20-2-8z"/></svg></button>
    </div>
  </div>
</footer>

</body>
</html>
```